Design eines Praxisschilds für Hausarztpraxis
Zielgruppe
Hausarztpraxis, Zielgruppe sind die Bewohner vor Ort, bodenständig
Aufgabenstellung
Praxisschild entwerfen, es soll schlicht sein. Das angefügte Logo bitte verwenden, ggf. auch nur das Symbol ohne Namen verwenden und den Namen extra in schwarz aufführen.
Farben:
- schwarz
- Pantone 13-0645 Limeade
- Pantone 7726
Text:
Dr. med. Heinrich Wolters
Facharzt für Innere Medizin
Facharzt für Allgemeinmedizin
Sprechzeiten:
Montag bis Freitag 07:30 – 12:00 Uhr
Dienstag und Donnerstag 17:00 – 19:00 Uhr
und nach Vereinbarung
Tel: 0761 83172
www.hausarzt-bergwinkel.de
Format quer (die Maße sind leider vorgegeben): 55,7 cm x 42,8 cm

```html
<!DOCTYPE html>
<html lang="de">
<head>
<meta charset="utf-8">
<title>Praxisschild – Dr. Heinrich Wolters</title>
<link rel="stylesheet" href="https://fonts.googleapis.com/css2?family=Poppins:wght@600;700&family=Barlow:wght@400;500&display=swap">
<style>
  :root {
    --ink: #262626;
    --forest: #007a48;
    --limeade: #d2dc55;
    --paper: #ffffff;
  }
  * { margin: 0; padding: 0; box-sizing: border-box; }
  html, body { width: 1200px; height: 922px; overflow: hidden; background: var(--paper); }
  .sign {
    position: relative;
    width: 1200px;
    height: 922px;
    background: var(--paper);
    border: 1px solid var(--ink);
    overflow: hidden;
  }
  .brand {
    position: absolute;
    top: 110px;
    left: 0;
    width: 100%;
    display: flex;
    justify-content: center;
    align-items: center;
    gap: 22px;
  }
  .brand-dot {
    width: 96px;
    height: 96px;
    border-radius: 50%;
    background: var(--forest);
  }
  .brand-name {
    font-family: "Barlow", sans-serif;
    font-weight: 500;
    font-size: 40px;
    color: var(--forest);
  }
  .doctor {
    position: absolute;
    top: 0;
    left: 0;
    width: 100%;
    text-align: center;
  }
  .doctor-name {
    position: absolute;
    top: 302px;
    width: 100%;
    font-family: "Poppins", sans-serif;
    font-weight: 700;
    font-size: 98px;
    line-height: 1;
    letter-spacing: -1px;
    color: var(--ink);
  }
  .doctor-title {
    position: absolute;
    top: 424px;
    width: 100%;
    font-family: "Barlow", sans-serif;
    font-weight: 500;
    font-size: 32px;
    line-height: 1;
    letter-spacing: 0.3px;
    color: var(--forest);
  }
  .info {
    position: absolute;
    left: 0;
    top: 498px;
    width: 100%;
    height: 424px;
    background: var(--forest);
    color: var(--paper);
    font-family: "Barlow", sans-serif;
    font-weight: 500;
  }
  .hours {
    position: absolute;
    left: 134px;
    top: 66px;
    font-size: 45px;
    line-height: 62px;
    letter-spacing: 0.5px;
  }
  .hours-row { display: flex; white-space: nowrap; }
  .hours-day { width: 560px; }
  .contact {
    position: absolute;
    left: 134px;
    top: 306px;
    width: 940px;
    display: flex;
    align-items: baseline;
    font-size: 45px;
    letter-spacing: 0.5px;
    white-space: nowrap;
  }
  .contact-phone { width: 387px; }
  .contact-web { color: var(--limeade); font-size: 40px; }
</style>
</head>
<body>
  <main class="sign">
    <div class="brand">
      <span class="brand-dot"></span>
      <span class="brand-name">Praxis Wolters</span>
    </div>

    <header class="doctor">
      <h1 class="doctor-name">Dr. Heinrich Wolters</h1>
      <p class="doctor-title">Facharzt für Innere Medizin | Facharzt für Allgemeinmedizin</p>
    </header>

    <section class="info">
      <div class="hours">
        <div class="hours-row"><span class="hours-day">Montag bis Freitag</span><span>07:30 – 12:00 Uhr</span></div>
        <div class="hours-row"><span class="hours-day">Dienstag und Donnerstag</span><span>17:00 – 19:00 Uhr</span></div>
        <div class="hours-row"><span>und nach Vereinbarung</span></div>
      </div>
      <div class="contact">
        <span class="contact-phone">Tel: 0761 83172</span>
        <span class="contact-web">www.hausarzt-bergwinkel.de</span>
      </div>
    </section>
  </main>
</body>
</html>
```